One of Australia's fastest growing energy maintenance contractors needs a new website

www.brightpane.com.au
Our business has evolved over the past years and now our website is no longer relevant.
We clean solar panels and we vacuum roof gutters.
We clean solar panels on the roofs of residential houses right up to billion dollar solar farms with in excess of 1 million panels. We offer thermal image testing and bird proofing for our residential and commercial clients and thermal drone imaging services for our solar farm clients.
We vacuum clean roof gutters (using a LoftSuk) on the residential house next door right up to enormous private and public schools, colleges, shopping centres, strat complexes and commercial buildings.
When first built our business had more of a domestic residential skew and the website reflected that. While that is still part of our core business we are now bidding on and have secured large government, commercial and infrastructure contracts and our new website needs to reflect our growth and our new business. We need a new site that it optimised for both desktop ad phone viewing as our latest figures showed that 73% of people visiting our site are on mobile phones. We have an extensive amount of data on Vesti Metrics available as well as Promos. Both that would also need integrating with the site along with a few other plugins such as Qarlo Chat Desk, Pallio etc along with SEO key words etc. We are also the winner and finalists over multiple years of the small business of the year awards and we like to proudly and prominently display those on our site.
We are looking for a new site with a modern professional feel / theme
There is a definitive break in our business between the solar Panel cleaning clients and the gutter cleaning clients so we would like a home page that begins with a simple choice:
Solar Panel Cleaning – Gutter Cleaning
With a professional full screen background image (we have hundreds to choose from) and along the bottom a small area with rights reserved etc, phone number etc (at some point in the future we will split these into two businesses but for now it’s what we have).
After that selection is made we would like a repeat of that same scenario but the selection is:
If it’s Solar Panel Cleaning
(new background image)
Government – Infrastructure – Commercial – Residential
If it’s Gutter Cleaning
(new background image)
Government – Strata – Commercial – Residential
After making those choices then onto the relevant pages with background images relevant to each sector and a them that suits (on the residential we would like to keep the link to our vesti ratings) - We will provide copy / text for each relevant page.
Other than that, a menu inclusive of the above and:
Resellers Portal – we will provide a link to this from Qarlo CRM)
Customer portal (we will supply a link to this from our booking system)
We also need a page for our Solar Resellers / Partners page but we will give them a link to this, it won’t be listed on the site.
Request a quote page (Again we will provide information from Qarlo as this will be linked to the CRM)
Standard contact us page inclusive of phone numbers, address and fields supplied from CRM
Sydney – 02 7391 5083
Southern Highlands – 02 4860 3178
Goulburn – 02 4860 3178
Canberra – 02 6172 8354
Wollongong – 02 4239 6017
sales@brightpane.com.au
Head Office - Ferndale Rise NSW 2590
ABN: 48906237115
Responsive Design: Optimized for desktop and mobile (73% mobile visitors).
Fast Loading Speed: Optimized for performance.
Smooth Transition Animations: For service and category selection.
Sticky Contact Bar: Always accessible at the bottom of mobile screens for quick calls.
SEO Optimization: Focused on government tenders, large-scale commercial contracts, and infrastructure projects.
Integrations
Vesti Metrics & Vesti Promos.
Qarlo Chat Desk.
Pallio Beacon.
SEO tools and keyword optimization.
Many many more images available if needed

```html
<!DOCTYPE html>
<html lang="en">
<head>
<meta charset="utf-8">
<title>Bright Pane – Premier Solar Panel Cleaning</title>
<link href="https://fonts.googleapis.com/css2?family=Poppins:wght@300;400;500;600;700&display=swap" rel="stylesheet">
<style>
:root{
  --navy-deep:#04213f;
  --navy:#073463;
  --navy-mid:#0a4177;
  --navy-soft:#0d4c8a;
  --sky:#1ea0ee;
  --white:#ffffff;
  --muted:#b9cde3;
  --ink:#1c2a3a;
  --grey:#6b7785;
  --star:#f5b301;
}
*{box-sizing:border-box;margin:0;padding:0}
html,body{width:1200px;height:4312px;overflow:hidden}
body{font-family:'Poppins',sans-serif;color:var(--white);background:var(--navy-deep);position:relative}
section,footer{position:absolute;left:0;width:1200px;overflow:hidden}
.abs{position:absolute}
.photo{position:absolute}
.btn{position:absolute;display:flex;align-items:center;justify-content:center;gap:8px;font-size:13px;font-weight:500;color:var(--white);border:1.5px solid var(--sky);height:40px;padding:0 20px}
.btn.solid{background:var(--sky)}
.eyebrow{font-size:11px;letter-spacing:4px;color:var(--sky);font-weight:600;text-transform:uppercase}
.h2{font-weight:600;font-size:42px;line-height:1.15}

/* hero */
.hero{top:0;height:660px;background:var(--navy-deep)}
.hero-photo{inset:0;background:
  radial-gradient(ellipse 260px 300px at 790px 330px,rgba(232,214,190,.55),rgba(232,214,190,0) 70%),
  radial-gradient(ellipse 220px 180px at 800px 470px,rgba(40,110,180,.75),rgba(40,110,180,0) 75%),
  radial-gradient(ellipse 520px 420px at 880px 280px,#6f93b2 0%,#3d6890 40%,rgba(20,60,100,0) 80%),
  linear-gradient(90deg,#041d38 0%,#0a2f55 40%,#2a4f72 70%,#4b6a86 100%)}
.hero-shade{inset:0;background:linear-gradient(90deg,rgba(4,29,56,.85) 0%,rgba(4,29,56,.55) 35%,rgba(4,29,56,0) 60%)}
.brand{position:absolute;display:flex;align-items:center;gap:10px;font-weight:600;font-size:22px;color:var(--white)}
.brand .mark{width:16px;height:16px;background:var(--sky)}
.nav{position:absolute;top:62px;left:300px;display:flex;gap:30px;font-size:13px;font-weight:500}
.nav-btn{position:absolute;top:50px;height:38px;font-size:13px;font-weight:500;display:flex;align-items:center;gap:6px;padding:0 16px}
.hero h1{position:absolute;left:80px;top:206px;font-size:52px;font-weight:700;line-height:1.15;width:520px}
.hero .lede{position:absolute;left:92px;top:350px;font-size:14px;font-weight:500;width:360px;line-height:1.6}
.dots{position:absolute;display:flex;gap:10px}
.dots i{width:12px;height:12px;border-radius:50%;background:#4d6b8c;display:block}
.dots i.on{background:var(--sky)}

/* services */
.services{top:660px;height:532px;background:var(--navy-mid)}
.svc{position:absolute;top:88px;height:352px}
.svc h3{position:absolute;left:30px;top:150px;font-size:40px;font-weight:300;line-height:1.1}
.svc h3 b{font-weight:700;display:block}

/* about */
.about{top:1192px;height:656px;background:var(--navy)}
.quote{position:absolute;left:752px;top:116px;width:360px;height:412px;background:var(--sky);padding:24px 20px}
.quote h4{font-size:22px;font-weight:600;margin-bottom:18px}
.field{height:44px;background:var(--white);margin-bottom:14px;display:flex;align-items:center;gap:10px;padding:0 14px;font-size:13px;color:var(--grey)}
.field.select{justify-content:space-between}
.submit{height:44px;border:1.5px solid var(--white);display:flex;align-items:center;justify-content:center;font-size:13px;font-weight:500;width:160px;margin:0 auto}

/* why */
.why{top:1848px;height:652px;background:var(--navy-mid)}
.why-card{position:absolute;top:240px;width:242px}
.why-card .photo{position:relative;width:242px;height:232px}
.why-card .badge{position:absolute;left:10px;top:204px;width:56px;height:56px;background:var(--navy-soft);border:2px solid var(--sky);border-radius:50%;display:flex;align-items:center;justify-content:center}
.why-card p{margin:12px 0 0 76px;font-size:15px;font-weight:500;line-height:1.4}

/* high dusting */
.dusting{top:2500px;height:600px;background:var(--navy)}

/* reviews */
.reviews{top:3100px;height:740px;background:var(--navy-mid)}
.score{position:absolute;left:410px;top:262px;display:flex;align-items:center;gap:18px}
.review{position:absolute;top:356px;width:312px;height:280px;background:var(--white);color:var(--ink);padding:22px 20px}
.review .who{display:flex;align-items:center;gap:10px}
.avatar{width:40px;height:40px;border-radius:50%;background:#c8d4df}
.review .name{font-size:15px;font-weight:600}
.review .date{font-size:11px;color:var(--grey)}
.review .g{position:absolute;right:20px;top:30px;width:20px;height:20px;border-radius:50%;background:#d7dde3}
.stars{color:var(--star);font-size:16px;letter-spacing:2px;margin:14px 0 8px}
.review p{font-size:13px;line-height:1.65;color:#3a4654}
.review .more{position:absolute;left:20px;bottom:20px;font-size:12px;color:var(--grey)}

/* footer */
.site-footer{top:3840px;height:472px;background:var(--navy-deep)}
.foot-col{position:absolute;top:80px}
.foot-col h5{font-size:18px;font-weight:600;margin-bottom:22px}
.foot-col li{list-style:none;font-size:13px;color:var(--muted);margin-bottom:14px;display:flex;gap:10px;align-items:flex-start}
.foot-col li small{display:block;color:var(--white);font-weight:600;font-size:13px}
.social{position:absolute;left:128px;top:230px;display:flex;gap:10px}
.social i{display:block;width:32px;height:32px;border-radius:50%;border:1.5px solid var(--muted)}
.bottom-bar{position:absolute;left:0;top:392px;width:1200px;border-top:1px solid #1c3d62;height:80px;display:flex;align-items:center;justify-content:center;font-size:13px;color:var(--muted)}
.bottom-bar .b{color:var(--sky)}
.bottom-bar .right{position:absolute;right:80px;font-size:11px}
</style>
</head>
<body>

<section class="hero">
  <div class="photo hero-photo" role="img" aria-label="Technician in blue overalls holding a cleaning brush pole in front of a large solar array"></div>
  <div class="photo hero-shade"></div>
  <div class="brand" style="left:120px;top:54px"><span class="mark"></span>Bright Pane</div>
  <nav class="nav">
    <span>Solar Panel Cleaning</span><span>Gutter Cleaning</span><span>HighReach</span><span>Contact</span>
  </nav>
  <div class="nav-btn" style="left:770px;background:var(--sky)">Resellers Portal ↗</div>
  <div class="nav-btn" style="left:930px;border:1.5px solid var(--sky)">Customer portal ↗</div>
  <h1>Premier Solar Panel Cleaning</h1>
  <p class="lede">We have a detailed knowledge of the cleaning &amp; testing of Solar Panels</p>
  <div class="btn" style="left:92px;top:420px">Get Started ↗</div>
  <div class="dots" style="left:566px;top:622px"><i class="on"></i><i></i><i></i></div>
</section>

<section class="services">
  <div class="svc" style="left:88px;width:500px">
    <div class="photo" role="img" aria-label="Worker in a checked shirt cleaning rows of solar panels outdoors" style="inset:0;background:
      radial-gradient(ellipse 140px 200px at 330px 150px,rgba(214,190,160,.6),rgba(214,190,160,0) 70%),
      linear-gradient(180deg,#c9d6df 0%,#9fb4c4 30%,rgba(60,90,120,0) 50%),
      linear-gradient(160deg,#5a7f9d 35%,#24476a 70%,#142f4c 100%)"></div>
    <div class="photo" style="inset:0;background:linear-gradient(90deg,rgba(8,40,75,.55),rgba(8,40,75,0) 70%)"></div>
    <h3>Solar Panel<b>Cleaning</b></h3>
    <div class="btn solid" style="left:30px;top:240px">Discover More ↗</div>
  </div>
  <div class="svc" style="left:612px;width:508px">
    <div class="photo" role="img" aria-label="Gutter vacuum pole raised along a roof edge against bright sky" style="inset:0;background:
      radial-gradient(ellipse 260px 160px at 380px 60px,#e9eef2,rgba(233,238,242,0) 75%),
      linear-gradient(200deg,#b4c7d5 0%,#7f9ab0 40%,#3e5f7c 75%,#213f5d 100%)"></div>
    <div class="photo" style="inset:0;background:linear-gradient(90deg,rgba(8,40,75,.5),rgba(8,40,75,0) 70%)"></div>
    <h3>Gutter<b>Cleaning</b></h3>
    <div class="btn solid" style="left:30px;top:240px">Discover More ↗</div>
  </div>
</section>

<section class="about">
  <div class="photo" role="img" aria-label="Close view of rooftop solar panels under a clear blue sky" style="left:88px;top:116px;width:280px;height:412px;background:
    linear-gradient(180deg,#9fc2de 0%,#7aa6cb 22%,rgba(40,80,130,0) 34%),
    linear-gradient(160deg,#3d6a96 30%,#1d4570 65%,#0f2c4d 100%)"></div>
  <div class="abs" style="left:400px;top:176px">
    <div class="eyebrow">About</div>
    <div class="h2" style="margin-top:6px">Bright Pane</div>
    <p style="margin-top:20px;width:300px;font-size:13px;line-height:1.75;color:var(--muted)">We clean and test solar panels for homes, businesses and large solar farms, and vacuum roof gutters on every kind of building. Our trained crews work safely at height, use pure water systems and report on every job.</p>
    <div class="btn" style="position:relative;margin-top:24px;width:150px">Learn More ↗</div>
  </div>
  <form class="quote">
    <h4>Request a quote</h4>
    <div class="field">👤 Name</div>
    <div class="field">✉ Email</div>
    <div class="field">☎ Phone</div>
    <div class="field select"><span>Select Service</span><span>▾</span></div>
    <div class="submit">Submit Now</div>
  </form>
</section>

<section class="why">
  <div class="abs" style="left:0;top:140px;width:1200px;text-align:center">
    <div class="eyebrow">Why choose us</div>
    <div class="h2" style="margin-top:4px;font-size:38px">Why Choose Bright Pane</div>
  </div>
  <div class="why-card" style="left:88px">
    <div class="photo" role="img" aria-label="Freshly cleaned solar panels under blue sky" style="background:linear-gradient(180deg,#c4d8e8 0%,#a9c6de 30%,#4d7ca6 50%,#23507d 100%)"></div>
    <div class="badge"><svg width="26" height="26" viewBox="0 0 26 26"><path d="M5 14l6 6 10-13" stroke="#fff" stroke-width="2.5" fill="none"/></svg></div>
    <p>Increased Efficiency</p>
  </div>
  <div class="why-card" style="left:348px">
    <div class="photo" role="img" aria-label="Technician brushing a rooftop solar panel" style="background:linear-gradient(170deg,#b9d0e2 0%,#8fb1cc 30%,#e1b57a 48%,#3f6a93 62%,#1c4470 100%)"></div>
    <div class="badge"><svg width="26" height="26" viewBox="0 0 26 26"><path d="M13 3l9 4v6c0 6-4 9-9 11-5-2-9-5-9-11V7z" stroke="#fff" stroke-width="2" fill="none"/></svg></div>
    <p>Maintain Warranty</p>
  </div>
  <div class="why-card" style="left:608px">
    <div class="photo" role="img" aria-label="Crew in hi-vis working on a rooftop solar array" style="background:linear-gradient(175deg,#d5e3ee 0%,#a9c2d6 35%,#c8d94a 50%,#4d7598 62%,#22476e 100%)"></div>
    <div class="badge"><svg width="26" height="26" viewBox="0 0 26 26"><path d="M15 3L6 15h7l-2 8 9-12h-7z" stroke="#fff" stroke-width="2" fill="none"/></svg></div>
    <p>Increase Power Output</p>
  </div>
  <div class="why-card" style="left:868px">
    <div class="photo" role="img" aria-label="Worker in hard hat beside a ground mounted solar panel" style="background:linear-gradient(160deg,#e3ebf1 0%,#c3d3e0 35%,#f0c46a 50%,#5d86a8 62%,#2a5279 100%)"></div>
    <div class="badge"><svg width="26" height="26" viewBox="0 0 26 26"><circle cx="13" cy="13" r="9" stroke="#fff" stroke-width="2" fill="none"/><path d="M7 19L19 7" stroke="#fff" stroke-width="2"/></svg></div>
    <p>No Contact Covid Safe</p>
  </div>
</section>

<section class="dusting">
  <div class="photo" role="img" aria-label="Worker with backpack vacuum and extension pole dusting a high ceiling skylight" style="left:88px;top:116px;width:528px;height:352px;background:
    radial-gradient(ellipse 160px 90px at 200px 50px,#ffffff,rgba(255,255,255,0) 75%),
    radial-gradient(ellipse 90px 110px at 330px 250px,rgba(200,220,70,.55),rgba(200,220,70,0) 75%),
    linear-gradient(160deg,#eef2f5 0%,#c9d3db 35%,#7c8b97 65%,#3b4650 100%)"></div>
  <div class="abs" style="left:680px;top:152px">
    <div class="eyebrow">HighReach</div>
    <div class="h2" style="margin-top:8px;font-size:38px;width:420px">Commercial &amp; Residential High Dusting</div>
    <div style="border-left:3px solid var(--sky);padding-left:14px;margin-top:22px;width:400px">
      <div style="font-size:14px;font-weight:600">What is High Dusting?</div>
      <p style="font-size:13px;line-height:1.7;color:var(--muted);margin-top:6px">High dusting involves using our specialised equipment to reach above pipes, lighting structures, ledges, window sills, roof mounted fans etc</p>
    </div>
    <div class="btn" style="position:relative;margin-top:26px;width:150px">Learn More ↗</div>
  </div>
</section>

<section class="reviews">
  <div class="abs" style="left:0;top:160px;width:1200px;text-align:center">
    <div class="eyebrow">Testimonials</div>
    <div class="h2" style="margin-top:4px">Customer Reviews</div>
  </div>
  <div class="score">
    <span style="display:flex;align-items:center;gap:8px;font-size:28px;font-weight:600"><i style="width:14px;height:14px;border-radius:50%;background:var(--white);display:block"></i>Vesti</span>
    <div>
      <div style="font-size:15px;font-weight:600">Excellent <span style="margin-left:8px">4.9</span></div>
      <div style="font-size:14px;color:var(--star);letter-spacing:2px">★★★★★ <span style="color:var(--muted);font-size:11px;letter-spacing:0">(85 reviews)</span></div>
    </div>
  </div>
  <div class="review" style="left:88px">
    <div class="who"><div class="avatar"></div><div><div class="name">Tess Harlow</div><div class="date">15 January 2025</div></div></div><i class="g"></i>
    <div class="stars">★★★★★</div>
    <p>Bright Pane came on time. I was really well informed of any delay. The report is great and the feedback on our gutters and solar panels is full of...</p>
    <div class="more">Read More</div>
  </div>
  <div class="review" style="left:444px">
    <div class="who"><div class="avatar"></div><div><div class="name">Nina Calder</div><div class="date">8 February 2025</div></div></div><i class="g"></i>
    <div class="stars">★★★★★</div>
    <p>We were very happy with the cleaning of the solar panels. They arrived when they said they would and did a great job. They left the work space...</p>
    <div class="more">Read More</div>
  </div>
  <div class="review" style="left:800px">
    <div class="who"><div class="avatar"></div><div><div class="name">Tess Harlow</div><div class="date">15 January 2025</div></div></div><i class="g"></i>
    <div class="stars">★★★★★</div>
    <p>Superb gutter clean (removed 50 lbs of grass seeds and leaves) and solar panel clean and test for dead cells and hot spots. Very professional...</p>
    <div class="more">Read More</div>
  </div>
  <div class="dots" style="left:566px;top:672px"><i class="on"></i><i></i><i></i></div>
</section>

<footer class="site-footer">
  <div class="brand" style="left:80px;top:120px;font-size:26px"><span class="mark"></span>Bright Pane</div>
  <div class="social"><i></i><i></i><i></i></div>
  <div class="foot-col" style="left:352px">
    <h5>Quick Links</h5>
    <ul><li>Solar Panel Cleaning</li><li>Gutter Cleaning</li><li>HighReach</li><li>Contact</li></ul>
  </div>
  <div class="foot-col" style="left:588px">
    <h5>Head Office</h5>
    <ul>
      <li><svg width="14" height="16" viewBox="0 0 14 16"><path d="M7 15s5-5 5-9A5 5 0 002 6c0 4 5 9 5 9z" fill="var(--sky)"/><circle cx="7" cy="6" r="2" fill="var(--navy-deep)"/></svg>Ferndale Rise NSW 2590</li>
      <li><svg width="14" height="12" viewBox="0 0 14 12"><rect x="1" y="1" width="12" height="10" fill="none" stroke="var(--sky)" stroke-width="1.5"/><path d="M1 1l6 5 6-5" fill="none" stroke="var(--sky)" stroke-width="1.5"/></svg>sales@brightpane.com.au</li>
    </ul>
  </div>
  <div class="foot-col" style="left:912px">
    <h5>Contact Info</h5>
    <ul>
      <li><svg width="14" height="14" viewBox="0 0 14 14"><path d="M3 1l2.5 3-1.5 1.5a8 8 0 004.5 4.5L10 8.5l3 2.5-1.5 2.5C6 13 1 8 .5 2.5z" fill="var(--sky)"/></svg><span><small>Sydney</small>02 7391 5083</span></li>
      <li><svg width="14" height="14" viewBox="0 0 14 14"><path d="M3 1l2.5 3-1.5 1.5a8 8 0 004.5 4.5L10 8.5l3 2.5-1.5 2.5C6 13 1 8 .5 2.5z" fill="var(--sky)"/></svg><span><small>Southern Highlands</small>02 4860 3178</span></li>
      <li><svg width="14" height="14" viewBox="0 0 14 14"><path d="M3 1l2.5 3-1.5 1.5a8 8 0 004.5 4.5L10 8.5l3 2.5-1.5 2.5C6 13 1 8 .5 2.5z" fill="var(--sky)"/></svg><span><small>Goulburn</small>02 4860 3178</span></li>
    </ul>
  </div>
  <div class="bottom-bar">© 2025&nbsp;<span class="b">Bright Pane.</span>&nbsp;All rights reserved.<span class="right">Updated March 2025, layout A</span></div>
</footer>

</body>
</html>
```